Law Firm in Texas in need of new letterhead

Law Firm in Fort Worth, TX, USA named "Pell & Whitcombe, Attorneys-At-Law, LLP." This is a general practice law firm that mostly does Family Law and Criminal Defense work.

We are looking for a new letterhead that has a "classical" appeal, with modern elements.

Any color combination is fine, but please note that we do fax many documents, so the design must be clearly legible in Black and White.

We would like our letterhead to project a sense of professionalism, integrity, and ability.

Target Market(s)

Letterhead will be for correspondence generally with other attorneys and clients.

Industry/Entity Type

Law Firm

Logo Text

Pell & Whitcombe, Attorneys-At-Law, LLP.

Logo styles of interest
Pictorial/Combination Logo
Wordmark Logo
Lettermark Logo
Requirements
Nice to have
• Although not necessary, a "Texas Star" that is incorporated into the design would be a nice touch.
Should not have
• Colors that do not convert to B&W easily

```html
<!DOCTYPE html>
<html lang="en">
<head>
<meta charset="utf-8">
<title>Pell &amp; Whitcombe — Letterhead</title>
<link href="https://fonts.googleapis.com/css2?family=Arimo:wght@400;700&display=swap" rel="stylesheet">
<style>
  :root {
    --paper: #ffffff;
    --ink: #000000;
    --ink-soft: #222222;
    --rule-dark: #4a4a4a;
    --band-light: #b3b3b3;
    --mark-soft: #e4e4e4;
    --mark-fade: #f7f7f7;
    --frame: #222222;
  }
  html, body {
    margin: 0;
    padding: 0;
    width: 1000px;
    height: 1200px;
    overflow: hidden;
    background: var(--paper);
  }
  .letterhead {
    position: relative;
    width: 1000px;
    height: 1200px;
    font-family: "Arimo", Arial, sans-serif;
    color: var(--ink);
  }
  .sheet-frame {
    position: absolute;
    left: 69px;
    top: 41px;
    width: 866px;
    height: 1121px;
    box-sizing: border-box;
    border: 1.5px solid var(--frame);
  }

  .band {
    position: absolute;
    left: 70px;
    width: 864px;
  }
  .band-header { top: 68px; height: 35px; background: var(--band-light); }
  .rule-header { top: 121px; height: 7px; background: var(--rule-dark); }
  .band-footer { top: 1100px; height: 35px; background: var(--band-light); }

  .firm-identity {
    position: absolute;
    right: 123px;
    top: 148px;
    text-align: right;
  }
  .firm-name {
    margin: 0;
    font-size: 28px;
    font-weight: 700;
    line-height: 34px;
    letter-spacing: -0.2px;
  }
  .firm-designation {
    margin: 0;
    font-size: 16px;
    font-weight: 700;
    line-height: 22px;
  }
  .firm-practice {
    margin: 0;
    font-size: 16px;
    font-weight: 400;
    line-height: 21px;
    color: var(--ink-soft);
  }

  .star-seal {
    position: absolute;
    left: 300px;
    top: 420px;
    width: 396px;
    height: 396px;
    border-radius: 50%;
    background: radial-gradient(circle, var(--mark-soft) 0%, var(--mark-fade) 72%, var(--mark-soft) 88%, var(--mark-fade) 100%);
    filter: blur(2px);
  }

  .firm-contact {
    position: absolute;
    left: 0;
    width: 1004px;
    top: 1044px;
    text-align: center;
    font-size: 16px;
    line-height: 23px;
  }
  .firm-contact p { margin: 0; }
  .firm-contact .gap { display: inline-block; width: 14px; }
</style>
</head>
<body>
  <main class="letterhead">
    <div class="band band-header"></div>
    <div class="band rule-header"></div>
    <div class="band band-footer"></div>

    <div class="sheet-frame"></div>

    <header class="firm-identity">
      <h1 class="firm-name">Pell &amp; Whitcombe</h1>
      <p class="firm-designation">Attorneys-at-Law LLP</p>
      <p class="firm-practice">Family Law &amp; Criminal Defense</p>
    </header>

    <div class="star-seal" role="img" aria-label="Faint Texas star seal watermark inside a circle"></div>

    <footer class="firm-contact">
      <p>2140 WEST LANCASTER AVENUE FORT WORTH TEXAS 76107</p>
      <p>T 817.555.0148<span class="gap"></span>F 817.555.0193</p>
    </footer>
  </main>
</body>
</html>
```